Business Cards for Financial Service Consulting Business Ltd

Business Card Design for my risk management consultancy to the financial service industry
Responsible Lending, Fair Charges, Ethical Collections

Should be serious, professional, corporate

Target Market(s)

Fintech, Financial Services Industry

Industry/Entity Type

Financial Service

Contact Information for Business Card

Marcus Pennick
marc@larchwellconsulting.co.uk
07700900418
01632960527

Font styles to use
Serif

Colors

Designer to choose colors to be used in the design.

Requirements
Must have
• Name: Larchwell Consulting
• Logo, contact details
• The three pillars of my business Responsible Lending, Fair Charges, Ethical Collections
Nice to have
• Corporate Feel
Should not have
• jokes, pretty pictures, cartoons

```html
<!DOCTYPE html>
<html lang="en">
<head>
<meta charset="utf-8">
<title>Larchwell Consulting – Business Cards</title>
<link rel="stylesheet" href="https://fonts.googleapis.com/css2?family=Open+Sans:wght@400;600;700&display=swap">
<style>
  :root {
    --backdrop: #ecebe8;
    --card: #ffffff;
    --brand-green: #6aaa3f;
    --text-grey: #555555;
    --rule-grey: #4a4a4a;
    --mark-grey: #8c8c8c;
  }
  * { margin: 0; padding: 0; box-sizing: border-box; }
  html, body {
    width: 1200px; height: 1000px; overflow: hidden;
    background: var(--backdrop);
    font-family: "Open Sans", Arial, sans-serif;
  }
  .canvas { position: relative; width: 1200px; height: 1000px; }
  .card {
    position: absolute; left: 266px; width: 666px; height: 397px;
    background: var(--card); border-radius: 28px;
    box-shadow: 0 4px 14px rgba(0,0,0,0.18);
    overflow: hidden;
  }
  .card--front { top: 74px; }
  .card--back { top: 533px; }

  .brand { position: absolute; text-align: center; }
  .brand__square {
    display: block; margin: 0 auto;
    border: 5px solid var(--mark-grey);
  }
  .brand__name {
    color: var(--brand-green); font-weight: 600;
    line-height: 1.1; letter-spacing: 1px;
  }

  .card--front .brand { left: 40px; width: 360px; top: 140px; }
  .card--front .brand__square { width: 60px; height: 60px; margin-bottom: 22px; }
  .card--front .brand__name { font-size: 34px; }

  .card--back .brand { left: 0; width: 666px; top: 80px; }
  .card--back .brand__square { width: 78px; height: 78px; margin-bottom: 28px; }
  .card--back .brand__name { font-size: 46px; }

  .contact { position: absolute; left: 368px; top: 120px; right: 0; }
  .contact__name {
    color: var(--brand-green); font-weight: 700; font-size: 21px;
    letter-spacing: 0.3px; padding-left: 0;
  }
  .contact__rule {
    height: 2px; background: var(--rule-grey); margin-top: 12px; margin-left: 2px;
  }
  .contact__list { list-style: none; margin-top: 34px; }
  .contact__item {
    display: flex; align-items: center; gap: 7px;
    color: var(--text-grey); font-size: 16px; height: 24px;
  }
  .contact__item--email { margin-top: 8px; }
  .contact__icon { width: 14px; height: 12px; fill: var(--brand-green); flex: none; }

  .tagline {
    position: absolute; left: 0; width: 666px; top: 348px;
    text-align: center; color: var(--text-grey); font-size: 16px;
  }
</style>
</head>
<body>
<main class="canvas">
  <section class="card card--front" aria-label="Front of business card">
    <div class="brand">
      <span class="brand__square"></span>
      <div class="brand__name">LARCHWELL<br>CONSULTING</div>
    </div>
    <div class="contact">
      <div class="contact__name">MARCUS PENNICK</div>
      <div class="contact__rule"></div>
      <ul class="contact__list">
        <li class="contact__item">
          <svg class="contact__icon" viewBox="0 0 14 12"><path d="M1 4 C1 1 13 1 13 4 L10 5 L9 3.5 H5 L4 5 Z M3 6 H11 L12.5 11 H1.5 Z"/></svg>
          07700900418
        </li>
        <li class="contact__item">
          <svg class="contact__icon" viewBox="0 0 14 12"><path d="M1 4 C1 1 13 1 13 4 L10 5 L9 3.5 H5 L4 5 Z M3 6 H11 L12.5 11 H1.5 Z"/></svg>
          01632960527
        </li>
        <li class="contact__item contact__item--email">
          <svg class="contact__icon" viewBox="0 0 14 12"><path d="M0 2 H14 V11 H0 Z" /><path d="M0.5 2.5 L7 7 L13.5 2.5" stroke="#fff" stroke-width="1.2" fill="none"/></svg>
          marc@larchwellconsulting.co.uk
        </li>
      </ul>
    </div>
  </section>

  <section class="card card--back" aria-label="Back of business card">
    <div class="brand">
      <span class="brand__square"></span>
      <div class="brand__name">LARCHWELL<br>CONSULTING</div>
    </div>
    <p class="tagline">Responsible Lending, Fair Charges, Ethical Collections</p>
  </section>
</main>
</body>
</html>
```